Construction material supplies company business card ****

1. Full company name “Marlow Aggregate Products Ltd”
I am after a Business card design for the company as a whole. We are better known in Solomon Islands as “Marlow Aggregate” for short.

We are a building materials supplier of
Ready Mixed Concrete, Bricks and Blocks,
Quarry products- gravel, aggregates, sand etc.
Cement distributor/retailer of reputable brands.
Other prefab concrete products. Culverts, wave breakers, concrete retaining blocks etc.

2. Competitive Advantage over Competition: Quality, efficient, professional, dependable, reliable

3. We want people to feel trust worthy, high quality, strong when they see our brand

5. No preference to color. Maybe more sturdy and corporate. Not fancy.

Industry/Entity Type

CONSTRUCTION SUPPLY

Contact Information for Business Card

Name, Position, office phone mob phone, email

Requirements
Must have
• the company logo
Nice to have
• would like to see a mixture of designs, of with logo only and also with simple graphic designs to bring out the company whilst still have the strong sturdy professional feeling

```html
<!DOCTYPE html>
<html lang="en">
<head>
<meta charset="utf-8">
<title>Marlow Aggregate – Business Cards</title>
<link href="https://fonts.googleapis.com/css2?family=Arimo:wght@400;700&display=swap" rel="stylesheet">
<style>
  :root {
    --navy: #17456c;
    --navy-deep: #133c5f;
    --white: #ffffff;
    --grey: #9a9a9a;
    --ink: #3a3a3a;
    --backdrop: #e8e5e0;
  }
  * { box-sizing: border-box; margin: 0; padding: 0; }
  html, body {
    width: 1200px; height: 900px; overflow: hidden;
    background: var(--backdrop);
    font-family: "Arimo", Arial, sans-serif;
  }
  .sheet {
    width: 1200px; height: 900px;
    display: flex; flex-direction: column; align-items: center; justify-content: center;
    gap: 56px;
  }
  .card {
    position: relative;
    width: 640px; height: 366px;
    overflow: hidden;
    box-shadow: 0 6px 18px rgba(0,0,0,0.18);
  }

  /* Front: navy card */
  .card--front { background: var(--navy); color: var(--white); }
  .brand {
    display: flex; align-items: center; gap: 16px;
    font-weight: 700; letter-spacing: 0.04em; text-transform: uppercase;
  }
  .brand__mark { display: block; flex: none; }
  .card--front .brand {
    position: absolute; left: 0; right: 0; top: 110px;
    justify-content: center; font-size: 40px;
  }
  .card--front .brand__mark { width: 34px; height: 34px; background: var(--white); }
  .product-list {
    position: absolute; left: 56px; bottom: 44px;
    font-size: 16px; line-height: 1.45;
  }
  .product-list__label { font-weight: 700; letter-spacing: 0.03em; }

  /* Back: white contact card */
  .card--contact { background: var(--white); color: var(--navy); }
  .card__wave { position: absolute; inset: 0; width: 100%; height: 100%; }
  .person { position: absolute; left: 44px; top: 46px; }
  .person__name { font-size: 24px; font-weight: 700; letter-spacing: 0.02em; text-transform: uppercase; }
  .person__role { font-size: 16px; color: var(--ink); margin-top: 2px; }
  .card--contact .brand {
    position: absolute; right: 40px; top: 88px;
    font-size: 32px; color: var(--navy);
  }
  .card--contact .brand__mark { width: 28px; height: 28px; background: var(--navy); }
  .contact-list {
    position: absolute; left: 44px; top: 196px;
    list-style: none; font-size: 17px; color: var(--ink); line-height: 1.55;
  }
  .contact-list li { display: flex; align-items: center; gap: 10px; }
  .contact-list svg { width: 16px; height: 16px; flex: none; }
  .tagline {
    position: absolute; right: 30px; bottom: 26px;
    text-align: right; color: var(--white); font-size: 15px; line-height: 1.45;
  }
</style>
</head>
<body>
<main class="sheet">

  <section class="card card--front" aria-label="Business card front">
    <div class="brand">
      <span class="brand__mark"></span>
      <span class="brand__name">Marlow Aggregate</span>
    </div>
    <div class="product-list">
      <p><span class="product-list__label">QUARRY PRODUCTS:</span> Gravel, Aggregates, sand etc.</p>
      <p><span class="product-list__label">CONCRETE PRODUCTS:</span> Culverts, Wave breakers</p>
      <p>Concrete retaining blocks etc.</p>
    </div>
  </section>

  <section class="card card--contact" aria-label="Business card back">
    <svg class="card__wave" viewBox="0 0 640 366" preserveAspectRatio="none" aria-hidden="true">
      <path d="M0 312 C 200 316 330 280 440 225 C 350 290 200 330 0 336 Z" fill="#9a9a9a"/>
      <path d="M0 336 C 220 336 380 290 640 140 L640 366 L0 366 Z" fill="#17456c"/>
    </svg>

    <div class="person">
      <p class="person__name">Daniel Harper</p>
      <p class="person__role">Managing Director</p>
    </div>

    <div class="brand">
      <span class="brand__mark"></span>
      <span class="brand__name">Marlow Aggregate</span>
    </div>

    <ul class="contact-list">
      <li>
        <svg viewBox="0 0 16 16" aria-hidden="true"><path d="M3 1.5 5.5 4 4.3 5.8c.8 2 2.2 3.4 4 4.2L10 8.8l2.5 2.5-1.4 2.3C6 13.2 2.6 9.5 1 4.7Z" fill="#17456c"/></svg>
        <span>044-555 210 347</span>
      </li>
      <li>
        <svg viewBox="0 0 16 16" aria-hidden="true"><rect x="4" y="1" width="8" height="14" rx="1.5" fill="none" stroke="#17456c" stroke-width="1.6"/><circle cx="8" cy="12.3" r="0.9" fill="#17456c"/></svg>
        <span>044-555 210 348</span>
      </li>
      <li>
        <svg viewBox="0 0 16 16" aria-hidden="true"><rect x="1" y="3.5" width="14" height="9" fill="#17456c"/><path d="M1 3.5 8 9l7-5.5" fill="none" stroke="#fff" stroke-width="1.2"/></svg>
        <span>info@marlowaggregate.com</span>
      </li>
    </ul>

    <div class="tagline">
      <p>Ready Mixed Concrete, Bricks and Blocks</p>
      <p>Cement distributor/retailer of reputable brands</p>
    </div>
  </section>

</main>
</body>
</html>
```